Author needs a new book, Kindle and Audiobook cover design

I updated and re-edited a book I wrote 25 years ago but now realize the title and design did not get the job done. I am seeking a book, Kindle and audiobook design that will make me stand out. The final design will pop while being sensitive to the nature of the subject. The title of the book is Quiet Lanterns. Subtitle: Ways to Notice and Step Away From Harmful Circles While Keeping Steady Belief by Dorian T. Wexcombe. I am wanting to get the attention of people who have been damaged by a church relationship that started well but ended badly.
Updates

The book title is: Quiet Lanterns. The Subtitle is: Ways To Notice and Step Away From Harmful Circles While Keeping Steady Belief. The dimension is 6x9 (150 pages) and I am the author: Dorian T. Wexcombe

Target Market(s)

People with a church experience; church leadership. Religious abuse victims.

Industry/Entity Type

Christian

Font styles to use
Serif

Colors

Designer to choose colors to be used in the design.

Requirements
Nice to have
• I am not married to the Serif font if another design works better.

```html
<!DOCTYPE html>
<html lang="en">
<head>
<meta charset="utf-8">
<title>Quiet Lanterns — Full Wrap Cover</title>
<link href="https://fonts.googleapis.com/css2?family=Oswald:wght@500;600;700&family=PT+Sans:ital,wght@0,400;0,700;1,700&family=Exo+2:wght@700&display=swap" rel="stylesheet">
<style>
  :root {
    --back-top: #4a3a38;
    --back-mid: #2a2226;
    --back-bottom: #1c1a22;
    --front-dark: #2b2a2a;
    --front-mid: #4a4846;
    --title-white: #ffffff;
    --accent-orange: #f0914a;
    --accent-lime: #c6f21c;
    --body-text: #f2eeee;
    --art-warm: #d9a25a;
    --art-stone: #c9b894;
    --art-shadow: #3a3230;
  }
  html, body {
    margin: 0;
    padding: 0;
    width: 1200px;
    height: 897px;
    overflow: hidden;
    background: #111;
  }
  .cover-wrap {
    position: relative;
    width: 1200px;
    height: 897px;
    overflow: hidden;
    font-family: "PT Sans", Arial, sans-serif;
  }

  /* Back cover */
  .back-cover {
    position: absolute;
    left: 0; top: 0;
    width: 614px; height: 897px;
    background: linear-gradient(180deg, var(--back-top) 0%, var(--back-mid) 45%, var(--back-bottom) 100%);
  }
  .back-title {
    position: absolute;
    left: 0; width: 578px;
    top: 52px;
    margin: 0;
    text-align: center;
    font-family: "Oswald", "Arial Narrow", sans-serif;
    font-weight: 600;
    font-size: 35px;
    line-height: 48px;
    letter-spacing: 1px;
    color: var(--accent-orange);
  }
  .back-subtitle {
    position: absolute;
    left: 0; width: 578px;
    top: 112px;
    margin: 0;
    text-align: center;
    white-space: nowrap;
    font-family: "Oswald", "Arial Narrow", sans-serif;
    font-weight: 600;
    font-size: 12.8px;
    line-height: 18px;
    text-transform: uppercase;
    color: var(--title-white);
  }
  .endorsements {
    position: absolute;
    left: 58px; top: 150px;
    width: 470px;
    margin: 0; padding: 0;
    list-style: none;
  }
  .endorsement {
    margin: 0 0 18px;
    font-size: 12.8px;
    line-height: 16.4px;
    color: var(--body-text);
  }
  .endorsement p { margin: 0; }
  .endorsement cite {
    display: block;
    font-style: italic;
    font-weight: 700;
    color: var(--accent-orange);
  }
  .author-photo {
    position: absolute;
    left: 58px; top: 616px;
    width: 171px; height: 242px;
    border: 2px solid #ffffff;
    background: linear-gradient(160deg, #2d3d6e 0%, #1a2448 60%, #5a5f6e 100%);
  }
  .author-bio {
    position: absolute;
    left: 290px; top: 607px;
    width: 262px;
    margin: 0;
    font-size: 12.8px;
    line-height: 16.4px;
    color: var(--body-text);
  }

  /* Spine */
  .spine {
    position: absolute;
    left: 564px; top: 0;
    width: 50px; height: 897px;
  }
  .spine-title,
  .spine-author {
    position: absolute;
    margin: 0;
    white-space: nowrap;
    transform-origin: 0 0;
    transform: rotate(90deg);
    color: var(--title-white);
  }
  .spine-title {
    top: 123px;
    left: 43px;
    font-family: "Oswald", "Arial Narrow", sans-serif;
    font-weight: 600;
    font-size: 20px;
    line-height: 24px;
    letter-spacing: 0.5px;
  }
  .spine-author {
    top: 700px;
    left: 42px;
    font-family: "PT Sans", Arial, sans-serif;
    font-weight: 700;
    font-size: 17px;
    line-height: 20px;
  }

  /* Front cover */
  .front-cover {
    position: absolute;
    left: 614px; top: 0;
    width: 586px; height: 897px;
    overflow: hidden;
    background: radial-gradient(ellipse at 55% 55%, var(--front-mid) 0%, var(--front-dark) 75%);
  }
  .front-art {
    position: absolute;
    left: 46px; top: 182px;
    width: 488px; height: 620px;
    border-radius: 244px 244px 16px 16px;
    background:
      radial-gradient(ellipse at 45% 55%, var(--art-warm) 0%, #b87a3c 35%, transparent 60%),
      linear-gradient(180deg, var(--art-stone) 0%, #a8946e 55%, var(--art-shadow) 100%);
  }
  .front-title {
    position: absolute;
    left: 0; width: 586px;
    top: 44px;
    margin: 0;
    text-align: center;
    white-space: nowrap;
    font-family: "Oswald", "Arial Narrow", sans-serif;
    font-weight: 700;
    font-size: 106px;
    line-height: 1.1;
    color: var(--title-white);
    transform: scaleX(0.7);
    transform-origin: 50% 0;
  }
  .front-subtitle {
    position: absolute;
    left: 50px; width: 486px;
    top: 182px;
    margin: 0;
    text-align: center;
    font-family: "Oswald", "Arial Narrow", sans-serif;
    font-weight: 600;
    font-size: 21px;
    line-height: 27px;
    text-transform: uppercase;
    color: var(--accent-lime);
    text-shadow: 0 1px 3px rgba(0,0,0,0.6);
  }
  .front-author {
    position: absolute;
    left: 0; width: 586px;
    top: 816px;
    margin: 0;
    text-align: center;
    font-family: "Exo 2", Arial, sans-serif;
    font-weight: 700;
    font-size: 34px;
    line-height: 44px;
    color: var(--accent-lime);
  }
</style>
</head>
<body>
<div class="cover-wrap">

  <section class="back-cover">
    <h2 class="back-title">QUIET LANTERNS</h2>
    <p class="back-subtitle">Ways to Notice and Step Away From Harmful Circles While Keeping Steady Belief</p>

    <ul class="endorsements">
      <li class="endorsement">
        <p>Dorian Wexcombe offers expert insight and a transparent evaluation in this book. With years of healthy involvement with that which is right in the body of Christ, he can speak to both the personal and systematic issues that cause bad environments to develop. The church landscape is littered with people who have been hurt in churches. This book will help clean things up.</p>
        <cite>- Harlan Pemberly, Senior Pastor, Cedar Hollow Fellowship, Ashford, VT. cedarhollowfc.org</cite>
      </li>
      <li class="endorsement">
        <p>“Seldom, if ever, have I read a book that was so refreshingly personal and real, yet delivered material that put you in a position to navigate the difficult and damaging challenges, of being part of a degenerating church. I was moved to tears and then lifted to a place of hope, by the pain and abuse that this family faced and their incredible testimony and journey of recovery. All glory to the power of His love for us.”</p>
        <cite>- Jora Vell, Kestrel Rise Ministries, kestrelrisejourneys.org</cite>
      </li>
      <li class="endorsement">
        <p>“Dorian Wexcombe offers a real-world view on how following your spiritual calling is not always easy but completely worth the journey. His down to earth approach allows the reader to process and be encouraged by his personal story, insight, and commitment to faith.”</p>
        <cite>- Selene Marrowick, Executive Director, Harbor Light Ministry, Inc. harborlightmin.org</cite>
      </li>
      <li class="endorsement">
        <p>“Dorian Wexcombe has been a pastor over 40 years. I have known him personally for many of those years. This book is a case study of how trust can be abused. Dorian handles this difficult issue with a good balance of honest introspection and critical analysis of leadership structures and practices. This book is a must-read.”</p>
        <cite>- Dalton R. Whitlow, ReasonedPath.com</cite>
      </li>
    </ul>

    <div class="author-photo" role="img" aria-label="Portrait photograph of the author"></div>

    <p class="author-bio">Dorian Wexcombe is a long-time pastor, author and podcaster who has impacted leaders and churches for many years. He wrote Iron Compass, a study of church leadership drawn from the history of the legendary ship. He and his wife Maren, together with their grown children and spouses all serve in ministry.</p>
  </section>

  <section class="spine">
    <p class="spine-title">QUIET LANTERNS</p>
    <p class="spine-author">Dorian T. Wexcombe</p>
  </section>

  <section class="front-cover">
    <div class="front-art" role="img" aria-label="Illustration of a dove flying out of an arched stone window with broken glowing panes and a candle on the sill"></div>
    <h1 class="front-title">QUIET LANTERNS</h1>
    <p class="front-subtitle">Ways To Notice and Step Away From Harmful Circles While Keeping Steady Belief</p>
    <p class="front-author">Dorian T. Wexcombe</p>
  </section>

</div>
</body>
</html>
```